Business card design needed

see my website

www.calderwoodandpike.com

I am after a new logo and business card needs to fit in with the website. I like the look of typewriter text - would like this on the website as well if I could!

Industry/Entity Type

Business

Contact Information for Business Card

Calderwood and Pike
Design and Heritage Consultants

Marcia Dowell
Principal

+61 437 690 215
marcia@calderwoodandpike.com

www.calderwoodandpike.com

back of card

Interior Design
Consultancy on Period Home restoration and renovation
Heritage Impact Statements
Conservation Management Plans
Materials Conservation
Historical Research

```html
<!DOCTYPE html>
<html lang="en">
<head>
<meta charset="utf-8">
<title>Calderwood and Pike – Business Card</title>
<link rel="stylesheet" href="https://fonts.googleapis.com/css2?family=Special+Elite&family=Courier+Prime&display=swap">
<style>
  :root {
    --teal: #1c9c9b;
    --teal-band: #1f9698;
    --ink: #161616;
    --paper: #f3f1ee;
    --photo-light: #efece8;
    --photo-mid: #dedad4;
    --photo-dark: #c9c4bd;
    --bar-black: #111111;
  }
  * { margin: 0; padding: 0; box-sizing: border-box; }
  html, body {
    width: 1200px;
    height: 741px;
    overflow: hidden;
    background: var(--paper);
  }
  .card {
    position: relative;
    width: 1200px;
    height: 741px;
    overflow: hidden;
    background: var(--paper);
  }
  .band-top {
    position: absolute;
    left: 0; top: 0;
    width: 1200px; height: 100px;
    background: var(--teal-band);
  }
  .band-bottom {
    position: absolute;
    left: 0; top: 725px;
    width: 1200px; height: 16px;
    background: var(--teal-band);
  }
  .band-bottom .accent-bar {
    position: absolute;
    left: 795px; top: 0;
    width: 302px; height: 16px;
    background: var(--bar-black);
  }
  .interior-photo {
    position: absolute;
    left: 0; top: 100px;
    width: 1200px; height: 625px;
    background:
      radial-gradient(ellipse 260px 200px at 560px 110px, rgba(255,255,255,0.9), rgba(255,255,255,0) 70%),
      radial-gradient(ellipse 380px 420px at 120px 260px, var(--photo-dark), rgba(201,196,189,0) 70%),
      radial-gradient(ellipse 300px 420px at 1080px 420px, var(--photo-mid), rgba(222,218,212,0) 75%),
      linear-gradient(180deg, var(--photo-light) 0%, var(--photo-mid) 100%);
  }
  .brand {
    position: absolute;
    left: 0; width: 1200px;
    top: 190px;
    text-align: center;
    padding-right: 30px;
  }
  .brand-name {
    font-family: "Special Elite", "Courier New", monospace;
    font-weight: 400;
    font-size: 84px;
    line-height: 1;
    letter-spacing: 2px;
    color: var(--teal);
  }
  .brand-tagline {
    margin-top: 24px;
    font-family: "Special Elite", "Courier New", monospace;
    font-weight: 400;
    font-size: 47px;
    line-height: 1;
    letter-spacing: 1px;
    color: var(--ink);
  }
  .contact {
    position: absolute;
    left: 0; width: 1248px;
    top: 408px;
    text-align: center;
    font-family: "Courier Prime", "Courier New", monospace;
    font-size: 28px;
    line-height: 41px;
    color: var(--ink);
    list-style: none;
  }
</style>
</head>
<body>
  <main class="card">
    <div class="band-top"></div>
    <div class="interior-photo" role="img" aria-label="Faded photograph of a weathered period home interior with hallway, doorways and staircase"></div>

    <header class="brand">
      <h1 class="brand-name">Calderwood and Pike</h1>
      <p class="brand-tagline">Heritage and Design Consultancy</p>
    </header>

    <ul class="contact">
      <li class="contact-company">Calderwood and Pike Design and Heritage</li>
      <li class="contact-person">Consultants Marcia Dowell Principal</li>
      <li class="contact-phone">+61 437 690 215</li>
      <li class="contact-email">marcia@calderwoodandpike.com</li>
      <li class="contact-web">www.calderwoodandpike.com</li>
    </ul>

    <div class="band-bottom">
      <div class="accent-bar"></div>
    </div>
  </main>
</body>
</html>
```